Local Realtors helping sellers and buyers make the right decision

Looking for an Ad to place in our local paper, that is completely different from the traditional ads we see from realtors. My mother and I are a team and we would like to really stand out from the rest of the ads. Ideally, one that has humor in it would be great. Being that it's the largest investment most people make in their lives, we want to show that hiring us is going to be the best move sellers and buyers will make. With over 50 years of experience as full time realtors between us. We want buyers and sellers to know that they don't just hire their friend or the first realtor they meet. You'll be hiring two full time agents that are in the trenches everyday and know how to help them navigate the ever changing market.
I'm attaching some meme's that I've seen online to give you an idea of what we're looking for in regards to being funny, yet professional. I am also attaching two typical ads that are in this newspaper. We promoting ourselves as Agents, and not homes specifically in this ad. Our head shots will be used as well as our company logo and other contact information. The size of the ad we have reserved is ( 1/2 page vertical (4.7 x 12.25 inches) Please let me know what else I you may need to help

Gregory Halvern Sales Associate greghomes@ravelmail.net Immediate Response # (555) 318-6047 Brookline Ridge Office 417 Marlow Street (555) 690-2174 Westfield, NJ 04815 Carol Halvern Sales Associate cmhalvern58@ravelmail.net Immediate Response # (555) 827-4390 Brookline Ridge Office 417 Marlow Street (555) 690-2174 Westfield, NJ 04815

Target Market(s)

Seller's and Buyers of residential property

Industry/Entity Type

Real Estate

Font styles to use
Serif

Colors
0555a3

Requirements
Must have
• Powerful, yet funny message to our targets
Nice to have
• We would like the ad to attract sellers and buyers
Should not have
• Should not be unprofessional. I know that's a broad description, but if you have to think about it not being professional, then it probably shouldn't be in there...

```html
<!DOCTYPE html>
<html lang="en">
<head>
<meta charset="utf-8">
<title>Halvern Team – Newspaper Ad</title>
<link rel="stylesheet" href="https://fonts.googleapis.com/css2?family=Fira+Sans+Extra+Condensed:ital,wght@0,700;1,700&family=Libre+Baskerville:wght@700&family=Tinos:ital,wght@0,400;0,700;1,700&display=swap">
<style>
  :root {
    --brand-blue: #0d52a0;
    --frame-blue: #1f57a0;
    --ink: #1a1a1a;
    --paper: #ffffff;
    --footer-grey: #efefef;
    --badge-dark: #222222;
    --stage-light: #ffffff;
    --stage-dark: #d6d6d6;
  }
  * { box-sizing: border-box; margin: 0; padding: 0; }
  html, body {
    width: 1200px; height: 900px; overflow: hidden;
    background: radial-gradient(ellipse at center, var(--stage-light) 40%, var(--stage-dark) 100%);
  }
  .ad {
    position: absolute; left: 444px; top: 10px;
    width: 332px; height: 883px;
    border: 2px solid var(--frame-blue);
    background: var(--paper);
    overflow: hidden;
  }
  .ad__headline { position: absolute; left: 0; top: 0; width: 328px; height: 300px; background: #f2f2f2; }
  .ad__headline-text {
    font-family: "Fira Sans Extra Condensed", "Arial Narrow", sans-serif;
    font-weight: 700; font-size: 45px; fill: #f4f4f4;
  }
  .ad__headline-shadow { fill: #0a2f5c; }
  .ad__subhead {
    position: absolute; left: 8px; top: 298px; width: 316px;
    font-family: "Libre Baskerville", Georgia, serif; font-weight: 700;
    font-size: 15.2px; line-height: 21px; letter-spacing: 0.6px;
    color: var(--brand-blue); text-transform: uppercase;
  }
  .ad__body {
    position: absolute; left: 8px; top: 369px; width: 314px;
    font-family: "Tinos", "Times New Roman", serif; font-size: 15.3px; line-height: 19.6px;
    color: var(--ink); text-align: justify;
  }
  .ad__body p + p { margin-top: 8px; }
  .agents {
    position: absolute; left: 0; top: 498px; width: 328px; height: 262px;
    background: var(--brand-blue);
  }
  .agent { position: absolute; left: 12px; width: 310px; height: 108px; }
  .agent--first { top: 14px; }
  .agent--second { top: 140px; }
  .agent__photo { position: absolute; left: 0; top: 0; width: 86px; height: 108px; }
  .agent__photo--him { background: linear-gradient(160deg, #3f5a2e 0%, #556b45 45%, #2f3b52 100%); }
  .agent__photo--her { background: linear-gradient(160deg, #6f8a4c 0%, #b39a78 45%, #6f8fc4 100%); }
  .agent__info {
    position: absolute; left: 95px; top: -1px;
    font-family: "Tinos", "Times New Roman", serif; color: #ffffff;
    font-size: 14px; line-height: 15.5px; letter-spacing: 0.4px;
  }
  .agent__name { font-weight: 700; font-size: 17.5px; line-height: 19px; letter-spacing: 0.5px; }
  .agent__title { font-style: italic; font-weight: 700; font-size: 13px; line-height: 14px; margin-bottom: 6px; }
  .agent__line + .agent__line { margin-top: 5px; }
  .agent__value { font-weight: 700; }
  .ad__footer {
    position: absolute; left: 0; top: 760px; width: 328px; height: 121px;
    background: var(--footer-grey);
  }
  .badge { position: absolute; background: var(--badge-dark); }
  .badge--housing { left: 8px; top: 12px; width: 66px; height: 72px; }
  .badge--member { left: 86px; top: 13px; width: 56px; height: 70px; }
  .brand {
    position: absolute; left: 154px; top: 11px; width: 168px; height: 72px;
    background: var(--brand-blue);
    display: flex; align-items: center; justify-content: center;
    font-family: "Tinos", "Times New Roman", serif; font-weight: 700;
    font-size: 21px; color: #ffffff; letter-spacing: 0.3px;
  }
  .brand__tagline {
    position: absolute; right: 8px; top: 94px;
    font-family: "Tinos", "Times New Roman", serif; font-size: 14px;
    color: var(--ink); letter-spacing: 0.2px;
    border-bottom: 1px solid var(--ink); padding-bottom: 1px;
  }
</style>
</head>
<body>
  <main class="ad">
    <header class="ad__headline">
      <svg width="328" height="300" viewBox="0 0 328 300" aria-label="Woo hoooooo, it's Friday! Oh wait... we're Realtors.">
        <polygon points="0,14 322,1 331,260 10,288" fill="var(--brand-blue)"/>
        <g transform="rotate(-4 10 60)">
          <g class="ad__headline-shadow ad__headline-text">
            <text x="12" y="80">Woo hoooooo,</text>
            <text x="14" y="136">it’s Friday!</text>
            <text x="18" y="194" font-style="italic">Oh wait...</text>
            <text x="20" y="252" font-style="italic">we’re Realtors.</text>
          </g>
          <g class="ad__headline-text">
            <text x="10" y="78">Woo hoooooo,</text>
            <text x="12" y="134">it’s Friday!</text>
            <text x="16" y="192" font-style="italic">Oh wait...</text>
            <text x="18" y="250" font-style="italic">we’re Realtors.</text>
          </g>
        </g>
      </svg>
    </header>

    <h2 class="ad__subhead">With over 50 years of experience as full time realtors between us.</h2>

    <section class="ad__body">
      <p>You'll be hiring two full time agents that are in the trenches everyday and know how to navigate the ever changing market.</p>
      <p>Being that it's the largest investment most people make in their lives, hiring us will be the best move a seller or buyer like you will make.</p>
    </section>

    <section class="agents">
      <article class="agent agent--first">
        <div class="agent__photo agent__photo--him" role="img" aria-label="Headshot of Gregory Halvern"></div>
        <div class="agent__info">
          <div class="agent__name">Gregory Halvern</div>
          <div class="agent__title">Sales Associate</div>
          <div class="agent__line">Immediate Response Cell:<br><span class="agent__value">(555) 318-6047</span></div>
          <div class="agent__line">Email:<br><span class="agent__value">greghomes@ravelmail.net</span></div>
        </div>
      </article>
      <article class="agent agent--second">
        <div class="agent__photo agent__photo--her" role="img" aria-label="Headshot of Carol Halvern"></div>
        <div class="agent__info">
          <div class="agent__name">Carol Halvern</div>
          <div class="agent__title">Sales Associate</div>
          <div class="agent__line">Immediate Response Cell:<br><span class="agent__value">(555) 827-4390</span></div>
          <div class="agent__line">Email:<br><span class="agent__value">cmhalvern58@ravelmail.net</span></div>
        </div>
      </article>
    </section>

    <footer class="ad__footer">
      <div class="badge badge--housing" role="img" aria-label="Fair housing badge"></div>
      <div class="badge badge--member" role="img" aria-label="Trade association membership badge"></div>
      <div class="brand">Harborline Realty</div>
      <div class="brand__tagline">RESIDENTIAL BROKERAGE</div>
    </footer>
  </main>
</body>
</html>
```